App für weniger Konsum
Zielgruppe
Wir sind ein Startup, das Nutzer:innen in einem bewussteren Kaufverhalten stärkt. Dabei werden Nutzer:innen psychologischen Kaufprofilen zugeordnet und individuell auf dem Weg begleitet, weniger einzukaufen. Das stärkt die Finanzen und schützt die Umwelt.
Aufgabenstellung
Das Design sollte einerseits minimalismusorientierte Nutzer:innen ansprechen (clean, ruhig), aber auch Nutzer:innen ansprechen, die sich noch nicht mit weniger / besserem Konsum beschäftigt haben.
Es wäre toll folgende Slides zu haben:
- Anmeldung / Registrierung
- Quiz (Es soll direkt zu Beginn ein Quiz aus mehreren Slides geben, das Nutzer:innen einem Kauftypen zuordnet(
- Quizergebnis (Du bist Kauftyp XYZ...)
- Home-Screen der App / Navigation
- Statistiken: Du hast diesen Monat so viel gespart...
- Slide mit Einstellungen
- 'Challenge' Slide: 10 tage aussortieren

```html
<!DOCTYPE html>
<html lang="de">
<head>
<meta charset="utf-8">
<title>KAUFRUH – App Screens</title>
<link href="https://fonts.googleapis.com/css2?family=Anton&family=Inter:wght@400;500;600&display=swap" rel="stylesheet">
<style>
:root{
  --brand:#84c3da;
  --brand-soft:#e4f2f8;
  --brand-deep:#4f9fbe;
  --ink:#1c1f22;
  --muted:#6f7880;
  --line:#e6eaed;
  --surface:#f3f6f8;
  --white:#ffffff;
}
*{box-sizing:border-box;margin:0;padding:0}
html,body{width:794px;height:1200px;overflow:hidden;background:var(--white)}
body{position:relative;font-family:"Inter",sans-serif;color:var(--ink)}
.screen{position:absolute;width:152px;height:333px;border-radius:20px;background:var(--white);border:1px solid var(--line);overflow:hidden}
.screen--brand{background:var(--brand);border-color:var(--brand)}
.abs{position:absolute}
.status{position:absolute;top:8px;left:0;right:0;height:10px}
.status__time{position:absolute;left:21px;top:0;font-size:6.5px;font-weight:600}
.status__icons{position:absolute;right:14px;top:1px}
.home-indicator{position:absolute;bottom:4px;left:50%;width:51px;height:2px;margin-left:-25.5px;border-radius:2px;background:var(--ink)}
.wordmark{position:absolute;left:0;right:0;text-align:center;font-family:"Anton",sans-serif;font-size:20px;letter-spacing:.3px;color:var(--brand)}
.headline{position:absolute;left:8px;right:8px;text-align:center;font-family:"Anton",sans-serif;text-transform:uppercase;color:var(--brand);font-size:23px;line-height:25px}
.headline--light{color:var(--white)}
.lead{position:absolute;left:12px;right:12px;text-align:center;font-size:5.5px;line-height:9px;color:var(--muted)}
.lead--light{color:var(--white)}
.btn{position:absolute;left:9px;right:9px;height:20px;border-radius:10px;background:var(--brand);color:var(--white);font-size:6.5px;font-weight:600;display:flex;align-items:center;justify-content:center}
.btn--white{background:var(--white);color:var(--brand)}
.btn--outline{background:var(--white);border:1px solid var(--line);color:var(--ink);font-weight:500;gap:5px}
.placeholder{position:absolute}
.title{position:absolute;left:9px;font-size:11px;font-weight:500}
.subtitle{position:absolute;left:9px;right:9px;font-size:4.8px;line-height:6.5px;color:var(--muted)}
.field{position:absolute;left:9px;right:9px;height:19px;border-radius:10px;background:var(--surface);font-size:6.5px;padding-left:9px;display:flex;align-items:center}
.tabs{position:absolute;left:9px;right:9px;top:73px;height:13px;border-radius:7px;background:var(--surface);display:flex;font-size:5px;color:var(--muted)}
.tabs span{flex:1;display:flex;align-items:center;justify-content:center}
.tabs .is-active{background:var(--brand);color:var(--white);border-radius:7px 0 0 7px;clip-path:polygon(0 0,88% 0,100% 50%,88% 100%,0 100%)}
.option{position:absolute;left:9px;right:9px;height:24px;border:1px solid var(--line);border-radius:4px;display:flex;align-items:center;gap:6px;padding:0 8px;font-size:5px;line-height:7px}
.radio{flex:none;width:6px;height:6px;border-radius:50%;background:var(--line)}
.radio--on{background:var(--white);box-shadow:inset 0 0 0 1.5px var(--brand-soft),inset 0 0 0 6px var(--brand)}
.sheet{position:absolute;left:0;right:0;top:194px;bottom:0;background:var(--white);border-radius:12px 12px 0 0}
.card{position:absolute;left:9px;right:9px;border:1px solid var(--line);border-radius:5px;background:var(--white)}
.card__head{background:var(--surface);color:var(--brand);font-size:6px;text-align:center;padding:5px 0;border-radius:5px 5px 0 0}
.amount{font-family:"Anton",sans-serif;color:var(--brand);font-size:14px}
.pill{display:inline-block;background:var(--brand-soft);color:var(--brand-deep);font-size:3.4px;padding:2px 4px;border-radius:5px;vertical-align:middle}
.band{position:absolute;left:0;right:0;height:16px;background:var(--surface);font-size:5px;display:flex;align-items:center;justify-content:center}
.section{position:absolute;left:9px;font-size:6.8px;font-weight:500}
.mini-card{position:absolute;top:161px;height:69px;width:64px;border:1px solid var(--line);border-radius:5px}
.mini-card__icon{position:absolute;left:5px;top:6px;width:12px;height:12px;border-radius:50%;background:var(--surface)}
.mini-card__go{position:absolute;right:0;top:7px;width:12px;height:10px;border-radius:5px 0 0 5px;background:var(--brand);color:var(--white);font-size:6px;display:flex;align-items:center;justify-content:center}
.mini-card__tag{position:absolute;left:5px;top:46px;font-size:3.8px;color:var(--brand)}
.mini-card__name{position:absolute;left:5px;top:53px;font-size:5.8px}
.quote{position:absolute;left:9px;right:9px;top:255px;height:38px;background:var(--surface);border-radius:4px 4px 0 0;padding:9px 8px 0}
.quote__text{font-family:"Anton",sans-serif;color:var(--brand);font-size:7.5px;line-height:10px;text-transform:uppercase}
.quote__mark{position:absolute;right:6px;top:-8px;font-family:"Anton",sans-serif;color:var(--brand);font-size:22px}
.nav{position:absolute;left:0;right:0;top:293px;height:40px;background:var(--white);border-top:1px solid var(--line);display:flex;padding:0 4px}
.nav__item{flex:1;display:flex;flex-direction:column;align-items:center;padding-top:6px;font-size:4.2px;color:#b8c0c6;position:relative}
.nav__item svg{width:11px;height:11px;margin-bottom:3px}
.nav__item.is-active{color:var(--brand)}
.nav__item.is-active::before{content:"";position:absolute;top:0;width:11px;height:1.5px;border-radius:1px;background:var(--brand)}
.chart{position:absolute;left:9px;right:9px;top:138px;height:108px}
.bar{position:absolute;bottom:12px;width:20px;border-radius:10px;background:repeating-linear-gradient(135deg,#eef6fa 0 1px,#f8fbfd 1px 3px);border:1px solid #e5f0f5}
.bar--peak{background:repeating-linear-gradient(135deg,#9bd0e3 0 1px,#cde8f2 1px 3px);border-color:var(--brand)}
.bar__value{position:absolute;top:-8px;left:0;right:0;text-align:center;font-size:3.6px;color:var(--brand)}
.bar__month{position:absolute;bottom:0;width:20px;text-align:center;font-size:4.2px;color:var(--brand)}
.challenge{position:absolute;left:9px;right:9px;height:64px;border:1px solid var(--line);border-radius:5px;padding:6px 5px 0}
.challenge__name{font-size:6px;font-weight:500}
.challenge__tag{font-size:4px;color:var(--brand);margin-top:3px}
.days{display:flex;gap:1.6px;margin-top:6px}
.days span{flex:1;height:6px;border-radius:2px;background:var(--brand-soft);color:var(--brand-deep);font-size:2.6px;display:flex;align-items:center;justify-content:center}
.days span.off{background:var(--surface);color:var(--muted)}
.challenge .btn{left:5px;right:5px;top:43px;height:13px;font-size:5px}
.setting{position:absolute;left:9px;right:11px;height:27px;border-bottom:1px solid var(--line);display:flex;align-items:center;gap:6px;font-size:6px}
.setting svg{width:10px;height:10px;flex:none}
.setting__chev{margin-left:auto;color:#b8c0c6;font-size:7px}
.info{display:flex;align-items:center;gap:4px;font-size:6px;font-weight:600}
.info i{width:7px;height:7px;border:.7px solid var(--brand);border-radius:50%;font-style:normal;font-size:4.5px;color:var(--brand);display:flex;align-items:center;justify-content:center}
</style>
</head>
<body>

<!-- Splash -->
<section class="screen" style="left:59px;top:74px">
  <div class="status"><span class="status__time">9:41</span><svg class="status__icons" width="26" height="6" viewBox="0 0 26 6"><rect x="0" y="4" width="1.5" height="2" fill="#1c1f22"/><rect x="2.5" y="3" width="1.5" height="3" fill="#1c1f22"/><rect x="5" y="1.5" width="1.5" height="4.5" fill="#1c1f22"/><rect x="7.5" y="0" width="1.5" height="6" fill="#1c1f22"/><path d="M11 2.2a5 5 0 0 1 6 0M12.3 3.7a3 3 0 0 1 3.4 0" stroke="#1c1f22" stroke-width="1" fill="none"/><circle cx="14" cy="5.2" r=".8" fill="#1c1f22"/><rect x="19" y="1" width="7" height="4" rx="1" fill="#1c1f22"/></svg></div>
  <div class="wordmark" style="top:125px">KAUFRUH</div>
  <svg class="abs" style="left:69px;top:191px" width="14" height="14" viewBox="0 0 14 14"><circle cx="7" cy="7" r="6" stroke="#e4f2f8" stroke-width="1.2" fill="none"/><path d="M7 1a6 6 0 0 0-6 6" stroke="#84c3da" stroke-width="1.2" fill="none"/></svg>
  <div class="home-indicator"></div>
</section>

<!-- Intro -->
<section class="screen" style="left:233.5px;top:74px">
  <div class="status"><span class="status__time">9:41</span><svg class="status__icons" width="26" height="6" viewBox="0 0 26 6"><rect x="0" y="4" width="1.5" height="2" fill="#1c1f22"/><rect x="2.5" y="3" width="1.5" height="3" fill="#1c1f22"/><rect x="5" y="1.5" width="1.5" height="4.5" fill="#1c1f22"/><rect x="7.5" y="0" width="1.5" height="6" fill="#1c1f22"/><path d="M11 2.2a5 5 0 0 1 6 0M12.3 3.7a3 3 0 0 1 3.4 0" stroke="#1c1f22" stroke-width="1" fill="none"/><circle cx="14" cy="5.2" r=".8" fill="#1c1f22"/><rect x="19" y="1" width="7" height="4" rx="1" fill="#1c1f22"/></svg></div>
  <div class="placeholder" role="img" aria-label="Illustration: brennender Geldschein in Blautönen" style="left:28px;top:38px;width:96px;height:138px;border-radius:40% 40% 48% 48%;background:radial-gradient(circle at 55% 45%,#a9d6e6,#d9eef6 65%,#ffffff 100%)"></div>
  <div class="headline" style="top:197px">Wie bewusst<br>kaufst du?</div>
  <div class="lead" style="top:257px">Lerne Dein Kaufverhalten kennen!</div>
  <div class="btn" style="top:284px">Continue</div>
  <div class="home-indicator"></div>
</section>

<!-- Login -->
<section class="screen" style="left:408px;top:74px">
  <div class="status"><span class="status__time">9:41</span><svg class="status__icons" width="26" height="6" viewBox="0 0 26 6"><rect x="0" y="4" width="1.5" height="2" fill="#1c1f22"/><rect x="2.5" y="3" width="1.5" height="3" fill="#1c1f22"/><rect x="5" y="1.5" width="1.5" height="4.5" fill="#1c1f22"/><rect x="7.5" y="0" width="1.5" height="6" fill="#1c1f22"/><path d="M11 2.2a5 5 0 0 1 6 0M12.3 3.7a3 3 0 0 1 3.4 0" stroke="#1c1f22" stroke-width="1" fill="none"/><circle cx="14" cy="5.2" r=".8" fill="#1c1f22"/><rect x="19" y="1" width="7" height="4" rx="1" fill="#1c1f22"/></svg></div>
  <div class="wordmark" style="top:72px">KAUFRUH</div>
  <div class="abs" style="left:0;right:0;top:135px;text-align:center;font-size:9px">Log in or Sign up</div>
  <div class="field" style="top:157px">emaildummy.com<span style="width:.7px;height:8px;background:var(--brand-deep);margin-left:1px"></span><span style="margin-left:auto;margin-right:7px;color:var(--brand);font-size:6px">×</span></div>
  <div class="btn" style="top:181px">Continue</div>
  <div class="abs" style="left:0;right:0;top:206px;text-align:center;font-size:5.5px;color:var(--muted)">or</div>
  <div class="btn btn--outline" style="top:219px"><span style="width:7px;height:7px;border-radius:50%;background:var(--brand)"></span>Continue with Lumio</div>
  <div class="btn btn--outline" style="top:242px"><span style="width:7px;height:7px;background:var(--ink)"></span>Continue with Orbix</div>
  <div class="home-indicator"></div>
</section>

<!-- Quiz intro -->
<section class="screen screen--brand" style="left:582px;top:74px">
  <div class="status"><span class="status__time">9:41</span><svg class="status__icons" width="26" height="6" viewBox="0 0 26 6"><rect x="0" y="4" width="1.5" height="2" fill="#1c1f22"/><rect x="2.5" y="3" width="1.5" height="3" fill="#1c1f22"/><rect x="5" y="1.5" width="1.5" height="4.5" fill="#1c1f22"/><rect x="7.5" y="0" width="1.5" height="6" fill="#1c1f22"/><path d="M11 2.2a5 5 0 0 1 6 0M12.3 3.7a3 3 0 0 1 3.4 0" stroke="#1c1f22" stroke-width="1" fill="none"/><circle cx="14" cy="5.2" r=".8" fill="#1c1f22"/><rect x="19" y="1" width="7" height="4" rx="1" fill="#1c1f22"/></svg></div>
  <div class="placeholder" role="img" aria-label="Illustration: weißes Gehirn" style="left:30px;top:55px;width:92px;height:88px;border-radius:46% 46% 40% 40%;background:radial-gradient(circle at 45% 40%,#ffffff,#e8eef1 60%,#c9dfe8 100%)"></div>
  <div class="headline headline--light" style="top:169px;font-size:21px;line-height:21px">Lass uns dein<br>Kaufverhalten<br>verstehen</div>
  <div class="lead lead--light" style="top:240px">Ein kurzer Quiz hilft uns, Empfehlungen zu geben, die zu deinen Gewohnheiten und Zielen passen.</div>
  <div class="btn btn--white" style="top:285px">Got it</div>
  <div class="home-indicator"></div>
</section>

<!-- Quiz -->
<section class="screen" style="left:59px;top:434px">
  <div class="status"><span class="status__time">9:41</span><svg class="status__icons" width="26" height="6" viewBox="0 0 26 6"><rect x="0" y="4" width="1.5" height="2" fill="#1c1f22"/><rect x="2.5" y="3" width="1.5" height="3" fill="#1c1f22"/><rect x="5" y="1.5" width="1.5" height="4.5" fill="#1c1f22"/><rect x="7.5" y="0" width="1.5" height="6" fill="#1c1f22"/><path d="M11 2.2a5 5 0 0 1 6 0M12.3 3.7a3 3 0 0 1 3.4 0" stroke="#1c1f22" stroke-width="1" fill="none"/><circle cx="14" cy="5.2" r=".8" fill="#1c1f22"/><rect x="19" y="1" width="7" height="4" rx="1" fill="#1c1f22"/></svg></div>
  <div class="title" style="top:32px">Wie konsumierst du?</div>
  <div class="subtitle" style="top:50px">Beantworte kurz 3 Fragen und erhalte eine kleine Einordnung.</div>
  <div class="tabs"><span class="is-active">Question 1</span><span>Question 2</span><span>Question 3</span></div>
  <div class="abs" style="left:9px;top:101px;font-size:6.8px">Wenn du etwas siehst, das du magst ...</div>
  <div class="option" style="top:117px"><span class="radio radio--on"></span>Ich kaufe es meist direkt.</div>
  <div class="option" style="top:146px"><span class="radio"></span>Ich lege es in den Warenkorb und überlege später.</div>
  <div class="option" style="top:174px"><span class="radio"></span>Ich notiere es und warte bewusst ab.</div>
  <div class="btn" style="top:286px;font-size:7px">Continue</div>
  <div class="home-indicator"></div>
</section>

<!-- Quiz result -->
<section class="screen screen--brand" style="left:233.5px;top:434px">
  <div class="status"><span class="status__time">9:41</span><svg class="status__icons" width="26" height="6" viewBox="0 0 26 6"><rect x="0" y="4" width="1.5" height="2" fill="#1c1f22"/><rect x="2.5" y="3" width="1.5" height="3" fill="#1c1f22"/><rect x="5" y="1.5" width="1.5" height="4.5" fill="#1c1f22"/><rect x="7.5" y="0" width="1.5" height="6" fill="#1c1f22"/><path d="M11 2.2a5 5 0 0 1 6 0M12.3 3.7a3 3 0 0 1 3.4 0" stroke="#1c1f22" stroke-width="1" fill="none"/><circle cx="14" cy="5.2" r=".8" fill="#1c1f22"/><rect x="19" y="1" width="7" height="4" rx="1" fill="#1c1f22"/></svg></div>
  <div class="placeholder" role="img" aria-label="Illustration: gläserner Haken in Blautönen" style="left:52px;top:32px;width:48px;height:40px;border-radius:10px;background:linear-gradient(135deg,#bfe1ee,#5f9fc0)"></div>
  <div class="headline headline--light" style="top:82px;font-size:21px;line-height:21px">Du bist ein<br>bewusster<br>Planer</div>
  <div class="lead lead--light" style="top:151px">Du legst Wert auf durchdachte Entscheidungen und langfristigen Nutzen statt spontaner Käufe.</div>
  <div class="sheet">
    <svg class="abs" style="left:72px;top:10px" width="9" height="7" viewBox="0 0 9 7"><path d="M1 1l3.5 3 3.5-3M1 3.5l3.5 3 3.5-3" stroke="#84c3da" stroke-width=".7" fill="none"/></svg>
    <div class="info abs" style="left:17px;top:29px;font-size:5.8px"><i>i</i>Description</div>
    <div class="abs" style="left:17px;right:17px;top:44px;font-size:4.8px;line-height:7.6px">Du denkst vor dem Kauf nach und überlegst, was deinem Leben wirklich Mehrwert bringt. Mit kleinen Anpassungen kannst du deine Gewohnheiten weiter stärken und noch mehr sparen – ganz ohne Verzichtsgefühl.</div>
    <div class="btn" style="top:101px">Continue to Home</div>
  </div>
  <div class="home-indicator"></div>
</section>

<!-- Home -->
<section class="screen" style="left:408px;top:434px">
  <div class="status"><span class="status__time">9:41</span><svg class="status__icons" width="26" height="6" viewBox="0 0 26 6"><rect x="0" y="4" width="1.5" height="2" fill="#1c1f22"/><rect x="2.5" y="3" width="1.5" height="3" fill="#1c1f22"/><rect x="5" y="1.5" width="1.5" height="4.5" fill="#1c1f22"/><rect x="7.5" y="0" width="1.5" height="6" fill="#1c1f22"/><path d="M11 2.2a5 5 0 0 1 6 0M12.3 3.7a3 3 0 0 1 3.4 0" stroke="#1c1f22" stroke-width="1" fill="none"/><circle cx="14" cy="5.2" r=".8" fill="#1c1f22"/><rect x="19" y="1" width="7" height="4" rx="1" fill="#1c1f22"/></svg></div>
  <div class="placeholder" role="img" aria-label="Profilfoto der Person" style="left:9px;top:30px;width:17px;height:17px;border-radius:50%;background:linear-gradient(160deg,#c9d3d8,#7f8c94)"></div>
  <div class="abs" style="left:32px;top:31px;font-size:5px;color:var(--muted)">Hello</div>
  <div class="abs" style="left:32px;top:39px;font-size:6.5px">Guten Morgen, User</div>
  <div class="abs" style="right:9px;top:31px;width:15px;height:15px;border-radius:50%;background:var(--surface);display:flex;align-items:center;justify-content:center"><svg width="6" height="7" viewBox="0 0 6 7"><path d="M1 5V3a2 2 0 0 1 4 0v2l.6.6H.4z" fill="#84c3da"/><circle cx="3" cy="6.3" r=".6" fill="#84c3da"/></svg></div>
  <div class="card" style="top:57px;height:59px">
    <div class="card__head">Diesen Monat gespart</div>
    <div class="abs" style="left:5px;top:20px"><span class="amount">€324</span> <span class="pill">↑ +€32 vs last month</span></div>
    <div class="abs" style="right:6px;top:28px;font-size:3.6px;color:var(--brand)">Statistic →</div>
    <div class="abs" style="left:5px;top:45px;font-size:4.5px">▢&nbsp; Vermiedene Impulskäufe: <b>6</b></div>
  </div>
  <div class="band" style="top:123px">Mach weiter</div>
  <div class="section" style="top:147px">Challenges</div>
  <div class="abs" style="right:9px;top:146px;font-size:7px;color:#b8c0c6">›</div>
  <div class="mini-card" style="left:9px"><span class="mini-card__icon"></span><span class="mini-card__go">→</span><span class="mini-card__tag">Aktive Challenge</span><span class="mini-card__name">10 Tage Ausmisten</span></div>
  <div class="mini-card" style="left:76px"><span class="mini-card__icon"></span><span class="mini-card__go">→</span><span class="mini-card__tag">Aktive Challenge</span><span class="mini-card__name">10 Tage Ausmisten</span></div>
  <div class="mini-card" style="left:144px"></div>
  <div class="section" style="top:243px">Heutige Intention</div>
  <div class="quote"><span class="quote__mark">“</span><div class="quote__text">Kaufe nur, was dir wirklich<br>Mehrwert bringt.</div></div>
  <nav class="nav">
    <span class="nav__item is-active"><svg viewBox="0 0 12 12"><path d="M2 5.5 6 2l4 3.5V10H2z" stroke="currentColor" stroke-width=".8" fill="none"/></svg>Home</span>
    <span class="nav__item"><svg viewBox="0 0 12 12"><path d="M2 10h8M3 10V6h2v4M5 10V3h2v7M7 10V5h2v5" stroke="currentColor" stroke-width=".8" fill="none"/></svg>Stats</span>
    <span class="nav__item"><svg viewBox="0 0 12 12"><path d="M1 10 5 4l2 3 1.5-2L11 10z" stroke="currentColor" stroke-width=".8" fill="none"/></svg>Challenges</span>
    <span class="nav__item"><svg viewBox="0 0 12 12"><circle cx="6" cy="6" r="4" stroke="currentColor" stroke-width=".8" fill="none"/><circle cx="6" cy="6" r="1.5" stroke="currentColor" stroke-width=".8" fill="none"/></svg>Settings</span>
  </nav>
  <div class="home-indicator"></div>
</section>

<!-- Stats -->
<section class="screen" style="left:582px;top:434px">
  <div class="status"><span class="status__time">9:41</span><svg class="status__icons" width="26" height="6" viewBox="0 0 26 6"><rect x="0" y="4" width="1.5" height="2" fill="#1c1f22"/><rect x="2.5" y="3" width="1.5" height="3" fill="#1c1f22"/><rect x="5" y="1.5" width="1.5" height="4.5" fill="#1c1f22"/><rect x="7.5" y="0" width="1.5" height="6" fill="#1c1f22"/><path d="M11 2.2a5 5 0 0 1 6 0M12.3 3.7a3 3 0 0 1 3.4 0" stroke="#1c1f22" stroke-width="1" fill="none"/><circle cx="14" cy="5.2" r=".8" fill="#1c1f22"/><rect x="19" y="1" width="7" height="4" rx="1" fill="#1c1f22"/></svg></div>
  <div class="title" style="top:32px">Dein Einfluss</div>
  <div class="subtitle" style="top:49px">Dein Fortschritt im Monatsüberblick</div>
  <div class="card" style="top:62px;height:43px">
    <div class="card__head">Diesen Monat gespart</div>
    <div class="abs" style="left:5px;top:20px"><span class="amount">€324</span> <span class="pill">↑ +€32 vs last month</span></div>
  </div>
  <div class="abs" style="left:9px;top:114px;font-size:6.5px">Your monthly savings over time</div>
  <div class="abs" style="left:9px;top:126px;font-size:4.2px">(Last 6 months)</div>
  <div class="chart">
    <div class="bar" style="left:0;height:80px"><span class="bar__value">€201</span></div>
    <div class="bar" style="left:23px;height:46px"><span class="bar__value">€57</span></div>
    <div class="bar" style="left:46px;height:89px"><span class="bar__value">€300</span></div>
    <div class="bar" style="left:69px;height:72px"><span class="bar__value">€194</span></div>
    <div class="bar" style="left:92px;height:84px"><span class="bar__value">€241</span></div>
    <div class="bar bar--peak" style="left:114px;height:96px"><span class="bar__value">€324</span></div>
    <span class="bar__month" style="left:0">Mar</span><span class="bar__month" style="left:23px">Apr</span><span class="bar__month" style="left:46px">May</span><span class="bar__month" style="left:69px">Jun</span><span class="bar__month" style="left:92px">Jul</span><span class="bar__month" style="left:114px">Aug</span>
  </div>
  <div class="info abs" style="left:9px;top:256px"><i>i</i>Erkenntnis</div>
  <div class="abs" style="left:9px;right:9px;top:269px;font-size:4.8px;line-height:7px">24 Stunden zu warten hat dir geholfen, die meisten Impulskäufe zu vermeiden.</div>
  <nav class="nav">
    <span class="nav__item"><svg viewBox="0 0 12 12"><path d="M2 5.5 6 2l4 3.5V10H2z" stroke="currentColor" stroke-width=".8" fill="none"/></svg>Home</span>
    <span class="nav__item is-active"><svg viewBox="0 0 12 12"><path d="M2 10h8M3 10V6h2v4M5 10V3h2v7M7 10V5h2v5" stroke="currentColor" stroke-width=".8" fill="none"/></svg>Stats</span>
    <span class="nav__item"><svg viewBox="0 0 12 12"><path d="M1 10 5 4l2 3 1.5-2L11 10z" stroke="currentColor" stroke-width=".8" fill="none"/></svg>Challenges</span>
    <span class="nav__item"><svg viewBox="0 0 12 12"><circle cx="6" cy="6" r="4" stroke="currentColor" stroke-width=".8" fill="none"/><circle cx="6" cy="6" r="1.5" stroke="currentColor" stroke-width=".8" fill="none"/></svg>Settings</span>
  </nav>
  <div class="home-indicator"></div>
</section>

<!-- Challenges -->
<section class="screen" style="left:59px;top:793.5px">
  <div class="status"><span class="status__time">9:41</span><svg class="status__icons" width="26" height="6" viewBox="0 0 26 6"><rect x="0" y="4" width="1.5" height="2" fill="#1c1f22"/><rect x="2.5" y="3" width="1.5" height="3" fill="#1c1f22"/><rect x="5" y="1.5" width="1.5" height="4.5" fill="#1c1f22"/><rect x="7.5" y="0" width="1.5" height="6" fill="#1c1f22"/><path d="M11 2.2a5 5 0 0 1 6 0M12.3 3.7a3 3 0 0 1 3.4 0" stroke="#1c1f22" stroke-width="1" fill="none"/><circle cx="14" cy="5.2" r=".8" fill="#1c1f22"/><rect x="19" y="1" width="7" height="4" rx="1" fill="#1c1f22"/></svg></div>
  <div class="abs" style="left:9px;right:9px;top:30px;height:17px;background:var(--surface);border-radius:5px 5px 0 0;color:var(--brand);font-size:6px;display:flex;align-items:center;justify-content:center">Ihre aktuelle Herausforderung</div>
  <div class="challenge" style="top:47px"><div class="challenge__name">10 Tage Ausmisten</div><div class="challenge__tag">Small daily steps toward mindful consumption</div><div class="days"><span>Day 1</span><span>Day 2</span><span>Day 3</span><span class="off">Day 4</span><span class="off">Day 5</span><span class="off">Day 6</span><span class="off">Day 7</span><span class="off">Day 8</span><span class="off">Day 9</span><span class="off">Day 10</span></div><div class="btn">Today’s task</div></div>
  <div class="challenge" style="top:115px"><div class="challenge__name">10 Tage Ausmisten</div><div class="challenge__tag">Small daily steps toward mindful consumption</div><div class="days"><span>Day 1</span><span>Day 2</span><span>Day 3</span><span class="off">Day 4</span><span class="off">Day 5</span><span class="off">Day 6</span><span class="off">Day 7</span><span class="off">Day 8</span><span class="off">Day 9</span><span class="off">Day 10</span></div><div class="btn">Today’s task</div></div>
  <div class="challenge" style="top:183px"><div class="challenge__name">10 Tage Ausmisten</div><div class="challenge__tag">Small daily steps toward mindful consumption</div><div class="days"><span>Day 1</span><span>Day 2</span><span>Day 3</span><span class="off">Day 4</span><span class="off">Day 5</span><span class="off">Day 6</span><span class="off">Day 7</span><span class="off">Day 8</span><span class="off">Day 9</span><span class="off">Day 10</span></div><div class="btn">Today’s task</div></div>
  <div class="challenge" style="top:251px"><div class="challenge__name">10 Tage Ausmisten</div><div class="challenge__tag">Small daily steps toward mindful consumption</div><div class="days"><span>Day 1</span><span>Day 2</span><span>Day 3</span><span class="off">Day 4</span><span class="off">Day 5</span><span class="off">Day 6</span><span class="off">Day 7</span><span class="off">Day 8</span><span class="off">Day 9</span><span class="off">Day 10</span></div></div>
  <nav class="nav">
    <span class="nav__item"><svg viewBox="0 0 12 12"><path d="M2 5.5 6 2l4 3.5V10H2z" stroke="currentColor" stroke-width=".8" fill="none"/></svg>Home</span>
    <span class="nav__item"><svg viewBox="0 0 12 12"><path d="M2 10h8M3 10V6h2v4M5 10V3h2v7M7 10V5h2v5" stroke="currentColor" stroke-width=".8" fill="none"/></svg>Stats</span>
    <span class="nav__item is-active"><svg viewBox="0 0 12 12"><path d="M1 10 5 4l2 3 1.5-2L11 10z" stroke="currentColor" stroke-width=".8" fill="none"/></svg>Challenges</span>
    <span class="nav__item"><svg viewBox="0 0 12 12"><circle cx="6" cy="6" r="4" stroke="currentColor" stroke-width=".8" fill="none"/><circle cx="6" cy="6" r="1.5" stroke="currentColor" stroke-width=".8" fill="none"/></svg>Settings</span>
  </nav>
  <div class="home-indicator"></div>
</section>

<!-- Settings -->
<section class="screen" style="left:233.5px;top:793.5px">
  <div class="status"><span class="status__time">9:41</span><svg class="status__icons" width="26" height="6" viewBox="0 0 26 6"><rect x="0" y="4" width="1.5" height="2" fill="#1c1f22"/><rect x="2.5" y="3" width="1.5" height="3" fill="#1c1f22"/><rect x="5" y="1.5" width="1.5" height="4.5" fill="#1c1f22"/><rect x="7.5" y="0" width="1.5" height="6" fill="#1c1f22"/><path d="M11 2.2a5 5 0 0 1 6 0M12.3 3.7a3 3 0 0 1 3.4 0" stroke="#1c1f22" stroke-width="1" fill="none"/><circle cx="14" cy="5.2" r=".8" fill="#1c1f22"/><rect x="19" y="1" width="7" height="4" rx="1" fill="#1c1f22"/></svg></div>
  <div class="title" style="top:31px">Einstellungen</div>
  <div class="setting" style="top:49px"><svg viewBox="0 0 10 10"><circle cx="5" cy="5" r="4.3" stroke="#84c3da" stroke-width=".6" fill="none"/><circle cx="5" cy="4" r="1.5" stroke="#84c3da" stroke-width=".6" fill="none"/></svg>Dein Kaufprofil<span class="setting__chev">›</span></div>
  <div class="setting" style="top:76px"><svg viewBox="0 0 10 10"><path d="M1 3h8M1 7h8M3 2v2M7 6v2" stroke="#84c3da" stroke-width=".6"/></svg>Einstellungen<span class="setting__chev">›</span></div>
  <div class="setting" style="top:104px"><svg viewBox="0 0 10 10"><path d="M2 7V5a3 3 0 0 1 6 0v2l1 1H1z" stroke="#84c3da" stroke-width=".6" fill="none"/></svg>Benachrichtigungen<span class="setting__chev">›</span></div>
  <div class="setting" style="top:131px"><svg viewBox="0 0 10 10"><circle cx="5" cy="5" r="4" stroke="#84c3da" stroke-width=".6" fill="none"/><circle cx="5" cy="5" r="2" stroke="#84c3da" stroke-width=".6" fill="none"/></svg>Ziele<span class="setting__chev">›</span></div>
  <div class="setting" style="top:159px"><svg viewBox="0 0 10 10"><rect x="1.5" y="4" width="7" height="5" stroke="#84c3da" stroke-width=".6" fill="none"/><path d="M3 4V3a2 2 0 0 1 4 0v1" stroke="#84c3da" stroke-width=".6" fill="none"/></svg>Daten &amp; Datenschutz<span class="setting__chev">›</span></div>
  <div class="setting" style="top:186px"><svg viewBox="0 0 10 10"><circle cx="5" cy="5" r="3.5" stroke="#84c3da" stroke-width=".6" fill="none" stroke-dasharray="1.5 .8"/><circle cx="5" cy="5" r="1.3" stroke="#84c3da" stroke-width=".6" fill="none"/></svg>App-Einstellungen<span class="setting__chev">›</span></div>
  <div class="setting" style="top:214px"><svg viewBox="0 0 10 10"><circle cx="5" cy="5" r="4" stroke="#84c3da" stroke-width=".6" fill="none"/><circle cx="5" cy="5" r="1.8" stroke="#84c3da" stroke-width=".6" fill="none"/></svg>Support<span class="setting__chev">›</span></div>
  <div class="abs" style="left:0;right:0;top:250px;text-align:center;font-size:4.8px;color:var(--muted)">Nutzungsbedingungen &amp; Datenschutz</div>
  <nav class="nav">
    <span class="nav__item"><svg viewBox="0 0 12 12"><path d="M2 5.5 6 2l4 3.5V10H2z" stroke="currentColor" stroke-width=".8" fill="none"/></svg>Home</span>
    <span class="nav__item"><svg viewBox="0 0 12 12"><path d="M2 10h8M3 10V6h2v4M5 10V3h2v7M7 10V5h2v5" stroke="currentColor" stroke-width=".8" fill="none"/></svg>Stats</span>
    <span class="nav__item"><svg viewBox="0 0 12 12"><path d="M1 10 5 4l2 3 1.5-2L11 10z" stroke="currentColor" stroke-width=".8" fill="none"/></svg>Challenges</span>
    <span class="nav__item is-active"><svg viewBox="0 0 12 12"><circle cx="6" cy="6" r="4" stroke="currentColor" stroke-width=".8" fill="none"/><circle cx="6" cy="6" r="1.5" stroke="currentColor" stroke-width=".8" fill="none"/></svg>Settings</span>
  </nav>
  <div class="home-indicator"></div>
</section>

</body>
</html>
```